Help design website for "Verdant Harbor Advisory" to advance the common good

Here is the Google doc link that lays out the design:

https://files.quillmarsh.net/doc/7TrWbnQe48XkLpZa2uMvYcD0sHfGjR35NwoEi9KxyBt/view?mode=share

Here is the Google drive folder with the logos and photos: https://store.quillmarsh.net/open?id=4K9pRtLmWqZx8825BvNcUaYeHs3Jd

The testimonials are being gathered and will be shared by Friday, 1/4.

The winner will also have to migrate the coding files to my hosting site.

Thank you for your help! Looking forward to seeing your designs.

Target Market(s)

Prospective clients

Industry/Entity Type

Non Profit

Coding

Coded - Design and coding required

Number of Pages Required

5+ page

Requirements
Must have
• Noted in the Google doc regarding layout.
Nice to have

```html
<!DOCTYPE html>
<html lang="en">
<head>
<meta charset="utf-8">
<title>Verdant Harbor Advisory</title>
<link rel="stylesheet" href="https://fonts.googleapis.com/css2?family=Jost:wght@300;400;600&family=Poppins:wght@400;500;600&display=swap">
<style>
:root{
  --ink:#2f323d;
  --ink-deep:#2a2d37;
  --blue:#3a8fd6;
  --bar:#3d9ad9;
  --paper:#f7fbfe;
  --text:#3c3f47;
  --frame:#5c6168;
  --white:#ffffff;
}
*{box-sizing:border-box;margin:0;padding:0}
html,body{width:1200px;height:1066px;overflow:hidden;background:var(--white)}
body{font-family:"Poppins",sans-serif;color:var(--text);position:relative}
.site-header{position:absolute;left:0;top:0;width:1200px;height:124px;background:var(--ink)}
.brand{position:absolute;left:225px;top:50px;display:flex;align-items:center;gap:12px}
.brand-mark{width:20px;height:20px;background:var(--blue)}
.brand-name{font-family:"Jost",sans-serif;font-weight:400;color:var(--white);font-size:21px;line-height:24px;white-space:nowrap}
.main-nav{position:absolute;left:582px;top:56px;display:flex;gap:11px;font-size:9.6px;color:#b9bdc4;font-weight:400;white-space:nowrap}
.main-nav .active{color:var(--white)}
.welcome{position:absolute;left:0;top:124px;width:1200px;height:458px;background:var(--paper)}
.welcome-title{position:absolute;left:0;width:1200px;text-align:center;top:18px;font-family:"Jost",sans-serif;font-weight:300;font-size:23px;color:var(--ink)}
.welcome-name{position:absolute;left:0;width:1200px;text-align:center;top:46px;font-family:"Jost",sans-serif;font-weight:600;font-size:24px;letter-spacing:1px;color:var(--blue)}
.portrait{position:absolute;left:234px;top:119px;width:294px;height:293px;border:4px solid var(--frame);background:linear-gradient(135deg,#9a8f83 0%,#6c5a4e 45%,#2d2a2c 100%)}
.intro{position:absolute;left:550px;top:118px;width:412px;font-size:8.7px;line-height:13.8px;letter-spacing:-0.05px}
.intro p{margin-bottom:13.8px}
.btn{position:absolute;left:551px;top:383px;width:93px;height:25px;background:var(--ink);color:var(--white);font-size:9px;font-weight:500;display:flex;align-items:center;justify-content:center}
.work{position:absolute;left:0;top:596px;width:1200px;height:400px;background:var(--ink)}
.work-title{position:absolute;left:0;width:1200px;text-align:center;top:30px;font-family:"Jost",sans-serif;font-weight:300;font-size:23px;color:var(--white)}
.work-title b{font-weight:600;color:var(--blue)}
.tile{position:absolute;width:231px;height:125px;background:var(--white);display:flex;align-items:center;justify-content:center;text-align:center;padding:0 14px;font-family:"Poppins",sans-serif;font-weight:600;font-size:15px;line-height:19px;color:var(--ink)}
.tile .dot{width:14px;height:14px;border-radius:50%;margin-right:8px;flex:none}
.social-bar{position:absolute;left:0;top:996px;width:1200px;height:38px;background:var(--bar);border-top:2px solid #cfe4f4;display:flex;justify-content:center;align-items:center;gap:24px;font-size:9px;font-weight:500;color:var(--white);letter-spacing:.3px}
.social-bar span{display:flex;align-items:center;gap:6px}
.social-bar i{width:7px;height:7px;border-radius:50%;background:var(--white);display:block}
.copyright{position:absolute;left:0;top:1034px;width:1200px;height:32px;background:var(--ink-deep);color:#d8dbe0;font-size:9.5px;display:flex;justify-content:center;align-items:center}
</style>
</head>
<body>
<header class="site-header">
  <div class="brand">
    <div class="brand-mark"></div>
    <div class="brand-name">Verdant Harbor Advisory</div>
  </div>
  <nav class="main-nav">
    <span class="active">HOME</span><span>ABOUT</span><span>SERVICES &amp; TESTIMONIALS</span><span>MEDIA &amp; IMPACT</span><span>CLIENTS</span><span>CONTACT</span>
  </nav>
</header>

<section class="welcome">
  <h1 class="welcome-title">WELCOME TO</h1>
  <h2 class="welcome-name">VERDANT HARBOR ADVISORY</h2>
  <div class="portrait" role="img" aria-label="Portrait photo of the founder outdoors"></div>
  <div class="intro">
    <p>Verdant Harbor Advisory supports nonprofit organizations and educational institutions to carry out their missions to benefit the wider community.</p>
    <p>Founder Mara Ellison is an educator with a 22-year record of demonstrated achievement and leadership roles in nonprofits and educational institutions. Most recently, she served as Associate Dean of Students in the University and Director of the Campus Civic Service Center at Lakeshore University. Mara has designed, implemented, and evaluated community-based learning and leadership training programs that have attained positive outcomes documented by survey results, recognition by outside agencies, and grants awarded for new initiatives and expansions. She has also significantly and consistently increased the number of program applicants, volunteers, and community partnerships through innovative programming, improved reputation, targeted recruitment, marketing and communications.</p>
    <p>Mara is a native Chicagoan and has also lived in Tokyo, Boston, San Francisco, and Washington, DC. Mara received her bachelor of arts from Whitfield College in Northfield, MN and her masters in education from Ashbury University in Cambridge, MA.</p>
  </div>
  <div class="btn">Keep Reading</div>
</section>

<section class="work">
  <h2 class="work-title">WORK <b>HISTORY</b></h2>
  <div class="tile" style="left:234px;top:89px"><span class="dot" style="background:#7a1113"></span>Campus Civic Service Center</div>
  <div class="tile" style="left:483px;top:89px"><span class="dot" style="background:#1e9ad6"></span>Meridian Fellows</div>
  <div class="tile" style="left:733px;top:89px"><span class="dot" style="background:#5bbb3c"></span>Brightpath Bay Schools</div>
  <div class="tile" style="left:234px;top:230px"><span class="dot" style="background:#e0a41c"></span>Civic Learners</div>
  <div class="tile" style="left:483px;top:230px"><span class="dot" style="background:#111111"></span>ServeNation Corps</div>
  <div class="tile" style="left:733px;top:230px"><span class="dot" style="background:#2a62a8"></span>Pacific Teaching Exchange</div>
</section>

<footer>
  <div class="social-bar">
    <span><i></i>GATHERLY</span><span><i></i>MURMUR</span><span><i></i>ORBITLY</span><span><i></i>SNAPFRAME</span><span><i></i>PINBOARDLY</span>
  </div>
  <div class="copyright">© 2019, All Rights Reserved, Verdant Harbor Advisory</div>
</footer>
</body>
</html>
```